Business Card Design for Fashion Tech Startup

Dear designers, we need a business card for Asia's premier fashion tech startup.!

PebbleHop is discovery e-commerce destination for busy, discerning parents in Asia featuring leading independent designers of baby, kids fashion apparel and sustainable brands from around the world.

PebbleHop is a modern, contemporary fashion tech startup targeting well-educated, well travelled and affluent parents. We're NOT your typical kiddy store!! Our design philosophy & e-commerce site is more like Vask.com, Orimesa.com, Pondwick.com, Farthollow.com.
Updates

Hi, size of the business card should be 84mm X 55mm. Would appreciate some business card layouts in Portrait as added consideration, i fancy the idea of a Portrait business card. What's important is that the business card should pique the receiver's interest to log onto the website to learn more. Many thanks and love forward to the designs!

Target Market(s)

Though modern, classy in look, feel & positioning, PebbleHop does possess a cheeky, fun-loving personality as depicted by its logo and the segment it targets (baby, kids) though the key decision makers i.e primarily mums between 25-40 who are well educated/travelled, local & expatriates, internet/digitally savvy, mid-high income working mums.

Industry/Entity Type

E-Commerce

Requirements
Must have
• Name, designation, email, phone & mobile number.
Company url : www.pebblehop.sg
Slogan : Discovery e-commerce destination for discerning, busy parents
Nice to have
• Call to Action such as a Discount code offering 10% discount
or asking people to "Like" us on our Chatterly page/Chatterly URL

```html
<!DOCTYPE html>
<html lang="en">
<head>
<meta charset="utf-8">
<title>PebbleHop Business Card</title>
<link rel="stylesheet" href="https://fonts.googleapis.com/css2?family=Open+Sans:wght@400;600;700;800&display=swap">
<style>
  :root {
    --slate: #2f4a5b;
    --coral: #f07560;
    --coral-soft: #f5a08f;
    --ink: #3a3a3a;
    --paper: #ffffff;
    --backdrop: #ece9e4;
    --rule: #d9d9d9;
  }
  * { box-sizing: border-box; margin: 0; padding: 0; }
  html, body {
    width: 1200px; height: 720px; overflow: hidden;
    background: var(--backdrop);
    font-family: "Open Sans", Arial, sans-serif;
  }
  .canvas {
    position: relative; width: 1200px; height: 720px;
  }
  .card {
    position: absolute; top: 183px;
    width: 540px; height: 354px;
    background: var(--paper);
    box-shadow: 0 2px 10px rgba(0,0,0,0.12);
    overflow: hidden;
  }
  .card--back { left: 40px; }
  .card--front { left: 620px; }

  /* Back card */
  .collage {
    position: absolute; left: 52px; top: 42px;
    width: 196px; height: 196px; border-radius: 50%;
    background: radial-gradient(circle at 50% 50%, var(--slate) 0 22%, var(--coral-soft) 23%, var(--coral) 60%, var(--slate) 100%);
    opacity: 0.9;
  }
  .divider {
    position: absolute; left: 290px; top: 34px;
    width: 1px; height: 170px; background: var(--rule);
  }
  .identity { position: absolute; left: 312px; top: 34px; }
  .identity__name {
    font-size: 19px; font-weight: 700; color: var(--slate); line-height: 1.2;
  }
  .identity__title {
    font-size: 13px; color: var(--coral); margin-top: 1px;
  }
  .contacts { list-style: none; margin-top: 16px; }
  .contacts li {
    display: flex; align-items: center; gap: 9px;
    font-size: 14px; color: var(--ink); line-height: 1; margin-bottom: 9px;
  }
  .contacts svg { width: 13px; height: 13px; flex: none; }
  .band-rule {
    position: absolute; left: 0; right: 0; top: 262px;
    height: 2px; background: var(--slate);
  }
  .slogan-band {
    position: absolute; left: 0; right: 0; top: 268px; bottom: 0;
    background: var(--coral);
    display: flex; align-items: center; justify-content: center;
    color: var(--paper); font-size: 16px; letter-spacing: 0.2px;
  }

  /* Front card */
  .brand {
    position: absolute; left: 0; right: 0; top: 118px;
    display: flex; align-items: center; justify-content: center; gap: 22px;
  }
  .brand__dot {
    width: 74px; height: 74px; border-radius: 50%; background: var(--coral);
  }
  .brand__name {
    font-size: 58px; font-weight: 800; color: var(--slate); letter-spacing: -0.5px;
  }
  .social {
    position: absolute; left: 0; right: 0; top: 268px;
    display: flex; align-items: center; justify-content: center; gap: 10px;
    font-size: 24px; color: var(--ink);
  }
  .social__mark {
    width: 22px; height: 22px; background: var(--slate);
  }
</style>
</head>
<body>
<main class="canvas">

  <section class="card card--back" aria-label="Business card, contact side">
    <div class="collage" role="img" aria-label="Round collage of baby clothing and toy icons around the brand name"></div>
    <div class="divider"></div>
    <div class="identity">
      <p class="identity__name">Your Name</p>
      <p class="identity__title">Title</p>
      <ul class="contacts">
        <li>
          <svg viewBox="0 0 14 14" aria-hidden="true"><circle cx="7" cy="7" r="7" fill="var(--coral)"/><path d="M4.6 3.6l1.4 1.6-.8.9c.5 1 1.3 1.8 2.3 2.3l.9-.8 1.6 1.4-.8 1.2C6.8 10 4 7.2 3.4 4.4z" fill="#fff"/></svg>
          012-555-0142
        </li>
        <li>
          <svg viewBox="0 0 14 14" aria-hidden="true"><circle cx="7" cy="7" r="7" fill="var(--coral)"/><rect x="5" y="3" width="4" height="8" rx="0.8" fill="#fff"/><rect x="5.8" y="4" width="2.4" height="5" fill="var(--coral)"/></svg>
          012-555-0142
        </li>
        <li>
          <svg viewBox="0 0 14 14" aria-hidden="true"><circle cx="7" cy="7" r="7" fill="var(--coral)"/><rect x="3.5" y="4.5" width="7" height="5" fill="#fff"/><path d="M3.5 4.5L7 7.3 10.5 4.5" fill="none" stroke="var(--coral)" stroke-width="0.9"/></svg>
          info@pebblehop.asia
        </li>
        <li>
          <svg viewBox="0 0 14 14" aria-hidden="true"><circle cx="7" cy="7" r="7" fill="var(--coral)"/><circle cx="7" cy="7" r="3.6" fill="none" stroke="#fff" stroke-width="1"/><path d="M3.4 7h7.2M7 3.4c-1.6 2-1.6 5.2 0 7.2M7 3.4c1.6 2 1.6 5.2 0 7.2" fill="none" stroke="#fff" stroke-width="0.8"/></svg>
          www.pebblehop.asia
        </li>
      </ul>
    </div>
    <div class="band-rule"></div>
    <p class="slogan-band">Discovery e-commerce destination for discerning, busy parents</p>
  </section>

  <section class="card card--front" aria-label="Business card, brand side">
    <div class="brand">
      <span class="brand__dot" aria-hidden="true"></span>
      <span class="brand__name">PebbleHop</span>
    </div>
    <p class="social">
      <span class="social__mark" aria-hidden="true"></span>
      /pebblehop.asia
    </p>
  </section>

</main>
</body>
</html>
```